Stationary

We have designed a new logo and business care.
It is now time for stationary.
We are a financial planning firm and are looking for something more formal that show the strength of our firm.
Please include our tag line; Integrity - Vision -Diligence.
I have uploaded a PDF of our current stationary - but - you are under no obligation to design anything like it.
Thx
Marta
Business

```html
<!DOCTYPE html>
<html lang="en">
<head>
<meta charset="utf-8">
<title>Northfield Trust Partners — Stationery</title>
<link href="https://fonts.googleapis.com/css2?family=Questrial&display=swap" rel="stylesheet">
<style>
:root{
  --navy:#343a85;
  --navy-dark:#2c3178;
  --blue:#2f7bc4;
  --paper:#f6f6f6;
  --ink:#444;
  --backdrop:#d2d2d2;
}
*{margin:0;padding:0;box-sizing:border-box}
html,body{width:1200px;height:1000px;overflow:hidden}
body{background:var(--backdrop);font-family:"Questrial",sans-serif;color:var(--ink);position:relative}
.piece{position:absolute;overflow:hidden}
.paper{background:var(--paper)}
.navy{background:var(--navy)}

.brand{text-align:center;white-space:nowrap}
.brand-name{display:flex;align-items:center;justify-content:center;gap:.35em;color:var(--navy)}
.brand-name .dot{width:.55em;height:.55em;border-radius:50%;background:var(--blue)}
.on-navy .brand-name{color:#fff}
.brand-tag{letter-spacing:.42em;color:var(--navy);margin-top:.35em}
.on-navy .brand-tag{color:#fff}

.wave{position:absolute;left:0;bottom:0;width:100%}

/* folder */
.folder{left:152px;top:42px;width:430px;height:558px;background:linear-gradient(90deg,var(--navy-dark),#3a4290 55%,var(--navy))}
.folder-spine{position:absolute;left:24px;top:0;bottom:0;width:4px;border-left:1px solid #262b6a;border-right:1px solid #454d9c}
.folder .brand{position:absolute;left:0;right:0;top:150px}
.folder .brand-name{font-size:20px}
.folder .brand-tag{font-size:8.5px}
.folder-url{position:absolute;left:0;right:0;bottom:44px;text-align:center;color:#fff;font-size:8px;letter-spacing:.02em}

/* letterhead */
.letterhead{left:616px;top:61px;width:417px;height:539px}
.letterhead .brand{position:absolute;left:27px;top:58px;text-align:left}
.letterhead .brand-name{font-size:12px;justify-content:flex-start}
.letterhead .brand-tag{font-size:5.5px}
.contact{position:absolute;font-size:5.2px;line-height:1.45;color:var(--ink)}
.contact .row{display:flex;align-items:center;gap:3px}
.icon{width:5px;height:5px;border-radius:1px;background:var(--blue)}
.letterhead .contact{right:28px;top:40px}
.letter{position:absolute;left:27px;right:27px;top:133px;font-size:5.6px;line-height:1.3}
.letter p{margin-bottom:7px}
.letter .date{margin-bottom:9px}
.letter .recipient{margin-bottom:31px}
.letter .salutation{font-weight:bold;margin-bottom:8px}
.signoff{position:absolute;left:27px;top:378px;font-size:5.6px;line-height:1.3}
.signoff strong{display:block}
.signature{position:absolute;left:82px;top:372px;width:92px;height:38px;background:linear-gradient(90deg,rgba(47,123,196,.10),rgba(52,58,133,.14));border-radius:3px}

/* envelope */
.envelope-front{left:117px;top:629px;width:466px;height:203px}
.envelope-front .brand{position:absolute;left:21px;top:43px;text-align:left}
.envelope-front .brand-name{font-size:10px;justify-content:flex-start}
.envelope-front .brand-tag{font-size:4.6px}
.envelope-front .address{position:absolute;left:49px;top:165px;font-size:5.2px;line-height:1.4;text-align:center}
.envelope-back{left:616px;top:629px;width:466px;height:203px}
.flap{position:absolute;left:0;top:0;width:100%;height:68px}
.flap-mark{position:absolute;left:0;right:0;top:22px;display:flex;justify-content:center;align-items:center;gap:4px;color:#fff;font-size:11px}
.flap-mark .dot{width:6px;height:6px;border-radius:50%;background:var(--blue)}

/* cards */
.card-back{left:410px;top:861px;width:172px;height:99px}
.card-back .brand{position:absolute;left:0;right:0;top:34px}
.card-back .brand-name{font-size:7.5px}
.card-back .brand-tag{font-size:3.4px}
.card-front{left:616px;top:861px;width:173px;height:99px}
.card-front .brand{position:absolute;left:8px;top:36px;width:96px}
.card-front .brand-name{font-size:6.8px}
.card-front .brand-tag{font-size:3.2px;letter-spacing:.35em}
.card-divider{position:absolute;left:109px;top:26px;width:1px;height:44px;background:#ccc}
.card-person{position:absolute;left:114px;top:27px;font-size:4.3px;line-height:1.45}
.card-person .name{font-weight:bold;color:var(--navy);font-size:5.2px}
.card-person .role{margin-bottom:4px}
.card-person .row{display:flex;align-items:center;gap:2px}
.card-person .icon{width:3.5px;height:3.5px}
.card-person .addr{margin-top:3px}
</style>
</head>
<body>

<section class="piece folder on-navy" aria-label="Presentation folder">
  <div class="folder-spine"></div>
  <div class="brand">
    <div class="brand-name"><span class="dot"></span>Northfield Trust Partners</div>
    <div class="brand-tag">Clarity Strength Prudence</div>
  </div>
  <div class="folder-url">www.NorthfieldTrust.com</div>
</section>

<section class="piece paper letterhead" aria-label="Letterhead">
  <div class="brand">
    <div class="brand-name"><span class="dot"></span>Northfield Trust Partners</div>
    <div class="brand-tag">Clarity Strength Prudence</div>
  </div>
  <div class="contact">
    <div class="row"><span class="icon"></span>(555) 014-2210</div>
    <div class="row"><span class="icon"></span>(555) 014-2211</div>
    <div style="margin-top:3px">220 Alder Row,<br>Brookfield, WA 99001</div>
  </div>
  <div class="letter">
    <p class="date">30.09.2016</p>
    <p class="recipient">Recipient's name<br>Lindenweg 4<br>20095 Hafen<br>Germany</p>
    <p class="salutation">Dear sir,</p>
    <p>Thank you for the time you gave us during our recent meeting at our office. We value the trust you place in our firm and wish to confirm the next steps of your financial plan in writing. This letter sums up what we discussed, the choices we reviewed together and the timeline we agreed on, so that you have a clear record to keep with your other papers and can refer to it whenever you need.</p>
    <p>Our advisers have reviewed your current holdings, income, expected expenses, goals and time horizon. Based on this review, we suggest a balanced approach that keeps steady income while allowing moderate growth over the coming years. We propose to shift part of your savings into a mix of bonds and broad market funds, to keep a cash reserve for short term needs, and to review your insurance cover before the end of the year. Each option carries its own level of risk, and we have set these out plainly in the enclosed summary. A full breakdown of fees, expected returns and tax effects is also enclosed with this letter for your reference.</p>
    <p>Please read the enclosed documents with care and note any questions you may have. We will gladly walk through every detail with you before any change is made, and nothing will proceed without your written approval. You may reach your adviser by phone or in person at any time during office hours.</p>
    <p>We look forward to continuing our work together and to helping you reach your goals with confidence. Should your plans or circumstances change, please let us know so that we can adjust your plan in good time. We thank you again for choosing our firm and for the confidence you have shown in our team.</p>
  </div>
  <div class="signoff">Yours Sincerely,<strong>Lena Corvin</strong></div>
  <div class="signature" role="img" aria-label="Handwritten signature of Lena Corvin"></div>
  <svg class="wave" viewBox="0 0 417 34" height="34" preserveAspectRatio="none" aria-hidden="true">
    <path d="M0 18 C140 16 270 -6 417 20 L417 24 C270 0 140 22 0 24Z" fill="var(--blue)"/>
    <path d="M0 34 L0 26 C150 26 260 -4 417 24 L417 34Z" fill="var(--navy)"/>
  </svg>
</section>

<section class="piece paper envelope-front" aria-label="Envelope front">
  <div class="brand">
    <div class="brand-name"><span class="dot"></span>Northfield Trust Partners</div>
    <div class="brand-tag">Clarity Strength Prudence</div>
  </div>
  <div class="address">220 Alder Row,<br>Brookfield, WA 99001</div>
  <svg class="wave" viewBox="0 0 466 30" height="30" preserveAspectRatio="none" aria-hidden="true">
    <path d="M0 12 C150 10 300 -6 466 20 L466 24 C300 0 150 18 0 20Z" fill="var(--blue)"/>
    <path d="M0 30 L0 22 C160 22 300 -2 466 26 L466 30Z" fill="var(--navy)"/>
  </svg>
</section>

<section class="piece paper envelope-back" aria-label="Envelope back">
  <svg class="flap" viewBox="0 0 466 68" preserveAspectRatio="none" aria-hidden="true">
    <path d="M0 0 L466 0 L452 58 Q449 66 440 66 L26 66 Q17 66 14 58 Z" fill="var(--navy)"/>
  </svg>
  <div class="flap-mark"><span class="dot"></span>NTP</div>
</section>

<section class="piece navy card-back on-navy" aria-label="Business card back">
  <div class="brand">
    <div class="brand-name"><span class="dot"></span>Northfield Trust Partners</div>
    <div class="brand-tag">Clarity Strength Prudence</div>
  </div>
</section>

<section class="piece paper card-front" aria-label="Business card front">
  <div class="brand">
    <div class="brand-name"><span class="dot"></span>Northfield Trust Partners</div>
    <div class="brand-tag">Clarity Strength Prudence</div>
  </div>
  <div class="card-divider"></div>
  <div class="card-person">
    <div class="name">JORDAN ELLERY</div>
    <div class="role">General Manager</div>
    <div class="row"><span class="icon"></span>(555) 014-2210</div>
    <div class="row"><span class="icon"></span>(555) 014-2211</div>
    <div class="addr">220 Alder Row,<br>Brookfield, WA 99001</div>
  </div>
  <svg class="wave" viewBox="0 0 173 14" height="14" preserveAspectRatio="none" aria-hidden="true">
    <path d="M0 6 C60 5 110 -2 173 8 L173 10 C110 0 60 8 0 9Z" fill="var(--blue)"/>
    <path d="M0 14 L0 11 C60 11 110 0 173 11 L173 14Z" fill="var(--navy)"/>
  </svg>
</section>

</body>
</html>
```